Powerpoint design for spirits and cosmetics packaging company

We need a powerpoint template that will be used for company presentations, projects, award ceremonies etc... We are packaging in the wine and spirits sector as well as in the cosmetics sector. Our job is to package our customers' bottles in gift boxes, to carry out labeling, quality control, etc. We are based in Cognac.
We work for the big names in luxury: QDRT, Vellane Ostrow, Trelumo, Syvanne etc...
The template should be neat with at least 10 different slides.
Cover page, summary page, product description page (several), page including a schedule, price presentation page.

Target Market(s)

premium spirits and cosmetics

Industry/Entity Type

Spiritueux et cosmétique

Font styles to use
Sans Serif

Requirements
Must have
• My project must have the logo attached, the possibility to add / modify photos afterwards. Must have about ten different slides

```html
<!DOCTYPE html>
<html lang="en">
<head>
<meta charset="utf-8">
<title>Maison Valcour — Presentation Template Overview</title>
<link href="https://fonts.googleapis.com/css2?family=Montserrat:wght@300;400;600;700;800;900&family=Open+Sans:wght@400;600&display=swap" rel="stylesheet">
<style>
:root{
  --red:#d8232c;
  --red-deep:#c31f2a;
  --orange:#f39a1e;
  --coral:#ea4a35;
  --ink:#333333;
  --muted:#5a5a5a;
  --white:#ffffff;
  --board:#6e7073;
  --grad:linear-gradient(135deg,#c41d2a 0%,#dc2e2f 55%,#ec5438 100%);
}
*{margin:0;padding:0;box-sizing:border-box}
html,body{width:1034px;height:1200px;overflow:hidden}
body{background:radial-gradient(circle at 50% 40%,#7b7d80,var(--board) 70%);font-family:'Montserrat',sans-serif;color:var(--ink);position:relative}
.slide{position:absolute;width:318px;height:178px;background:var(--white);overflow:hidden;box-shadow:0 2px 5px rgba(0,0,0,.45)}
.abs{position:absolute}
.photo{position:absolute}
.ph-amber{background:linear-gradient(140deg,#5f6d78 0%,#9b7b55 45%,#c8954e 70%,#4a3a2c 100%)}
.ph-bottle{background:linear-gradient(160deg,#d9d3cb 0%,#8c6a44 45%,#3b2a1e 80%,#bdb5ab 100%)}
.ph-factory{background:linear-gradient(150deg,#8c9aa8 0%,#b8c0c6 40%,#6f7b86 70%,#a09a92 100%)}
.ph-line{background:linear-gradient(120deg,#55626e 0%,#a7b1b9 45%,#d9dde0 75%,#c6ccd1 100%)}
.ph-cognac{background:linear-gradient(150deg,#c9c2b6 0%,#a6622a 45%,#6e3414 75%,#d2cbc2 100%)}
.ph-red{background:var(--grad)}
.mini-logo{position:absolute;top:7px;right:8px;display:flex;align-items:center;gap:2px;font:700 3.1px/1.1 'Montserrat',sans-serif;color:var(--red)}
.mini-mark{width:7px;height:7px;border:1.2px solid var(--red)}
.mini-logo.on-red{background:var(--white);padding:2px 3px}
.pg{position:absolute;right:7px;bottom:6px;font:700 3.8px/1 'Montserrat',sans-serif;color:var(--red);border:.8px solid var(--red);border-left-color:transparent;border-top-color:transparent;padding:1.5px 2px}
.pg.light{color:var(--white);border-color:var(--white);border-left-color:transparent;border-top-color:transparent}
.tx{font:400 3px/1.38 'Open Sans',sans-serif;color:var(--muted)}
.tx.j{text-align:justify}
.tx.w{color:var(--white)}
.tx.c{text-align:center}
.kick{font:400 9px/1 'Montserrat',sans-serif;color:var(--orange)}
.head{font:800 14px/1 'Montserrat',sans-serif;color:var(--red)}
.sub{font:700 5.6px/1 'Montserrat',sans-serif;color:var(--orange)}
.bullet{display:flex;gap:3px}
.bullet i{flex:none;width:0;height:0;border-left:3.5px solid var(--red);border-top:2px solid transparent;border-bottom:2px solid transparent;margin-top:1px}
.bullet.w i{border-left-color:var(--white)}
.frame-l{position:absolute;border-left:2px solid var(--red);border-bottom:2px solid var(--red)}
.frame-r{position:absolute;border-top:2px solid var(--red);border-right:2px solid var(--red)}
.social{display:flex;gap:3px}
.social span{width:9px;height:9px;background:var(--red);border-radius:1.5px}

/* brand lockup: plain square + name */
.brand{display:flex;gap:6px;align-items:center}
.brand-square{flex:none;width:18px;height:18px;border:2.5px solid var(--red)}
.brand-name{font:600 9px/1.1 'Montserrat',sans-serif;color:var(--red);letter-spacing:.8px}
.cover-business{left:17px;top:122px;font:900 21px/1 'Montserrat',sans-serif;color:var(--red)}
.cover-marketing{left:152px;top:124px;font:900 18.5px/1 'Montserrat',sans-serif;color:var(--orange)}
.url{font:600 4.3px/1 'Montserrat',sans-serif;letter-spacing:1.6px;color:var(--red)}

.toc-item{position:absolute;left:158px;width:140px}
.toc-item b{font:800 7.5px/1 'Montserrat',sans-serif;color:var(--red);margin-right:3px}
.toc-item strong{font:700 6.6px/1 'Montserrat',sans-serif;color:var(--orange)}
.toc-item p{margin:2px 0 0 11px}

.icon-dot{position:absolute;width:24px;height:24px;border-radius:50%;background:var(--orange);border:2.5px solid var(--white);box-shadow:0 0 0 1px var(--orange)}

.edu-box{position:absolute;top:44px;width:57px;height:85px;border:1.6px solid var(--red);border-radius:6px;background:rgba(255,255,255,.85);padding:14px 4px 0;text-align:center}
.edu-box.or{border-color:var(--orange)}
.edu-box h4{font:700 4.4px/1 'Montserrat',sans-serif;color:var(--red);margin:3px 0 2.5px}

.legend h5{font:600 4.4px/1 'Montserrat',sans-serif;color:var(--orange);display:flex;align-items:center;gap:3px}
.legend h5::before{content:"";width:3.5px;height:3.5px;border-radius:50%;background:currentColor}
.legend h5.r{color:var(--red)}
.legend p{margin:2px 0 0 6.5px}

.check{display:flex;gap:5px;font:400 6.8px/1 'Open Sans',sans-serif;color:var(--ink);position:absolute;left:171px}
.check svg{flex:none}

.member{position:absolute;top:80px;width:52px;text-align:center}
.avatar{width:24px;height:24px;border-radius:50%;margin:0 auto;background:linear-gradient(160deg,#e9d7c6,#9a7b64);border:1.8px solid var(--white)}
.member h6{font:700 4.6px/1 'Montserrat',sans-serif;color:var(--orange);margin:4px 0 2px}
</style>
</head>
<body>

<!-- 01 Cover -->
<section class="slide" style="left:29px;top:34px">
  <div class="abs brand" style="left:16px;top:26px">
    <span class="brand-square"></span>
    <span class="brand-name">MAISON<br>VALCOUR</span>
  </div>
  <div class="photo ph-amber" style="left:147px;top:0;width:171px;height:178px" role="img" aria-label="Photo of hands sealing the cap of a spirits bottle"></div>
  <div class="abs social" style="left:266px;top:18px"><span></span><span></span></div>
  <div class="frame-r" style="left:272px;top:8px;width:28px;height:24px"></div>
  <div class="abs kick" style="left:17px;top:107px;font-size:10.5px">PRESENTATION</div>
  <div class="abs cover-business">BUSINESS</div>
  <div class="abs cover-marketing">MARKETING</div>
  <div class="frame-l" style="left:7px;top:108px;width:140px;height:63px"></div>
  <div class="abs url" style="left:17px;top:156px">www.maisonvalcour.com</div>
</section>

<!-- 02 Contents -->
<section class="slide" style="left:359px;top:34px">
  <div class="photo ph-bottle" style="left:0;top:0;width:122px;height:178px" role="img" aria-label="Photo of a dark rum bottle on a packing line"></div>
  <div class="abs" style="left:68px;top:76px;background:var(--white);padding:3px 4px;font:800 17px/1 'Montserrat',sans-serif;color:var(--red)">Contents</div>
  <div class="mini-logo"><span class="mini-mark"></span><span>MAISON<br>VALCOUR</span></div>
  <div class="toc-item" style="top:30px"><b>1.</b><strong>Lorem ipsum</strong><p class="tx">We pack, label and check every bottle with care for premium brands.</p></div>
  <div class="toc-item" style="top:66px"><b>2.</b><strong>Lorem ipsum</strong><p class="tx">We pack, label and check every bottle with care for premium brands.</p></div>
  <div class="toc-item" style="top:98px"><b>3.</b><strong>Lorem ipsum</strong><p class="tx">We pack, label and check every bottle with care for premium brands.</p></div>
  <div class="toc-item" style="top:132px"><b>4.</b><strong>Lorem ipsum</strong><p class="tx">We pack, label and check every bottle with care for premium brands.</p></div>
  <span class="pg">02</span>
</section>

<!-- 03 Part One -->
<section class="slide ph-red" style="left:688px;top:34px" role="img" aria-label="Red tinted photo of a packing workshop">
  <div class="mini-logo on-red"><span class="mini-mark"></span><span>MAISON<br>VALCOUR</span></div>
  <svg class="abs" style="left:0;top:0" width="318" height="178">
    <path d="M136 49 H104 V151 H214 V49 H183" fill="none" stroke="#fff" stroke-width="1.4"/>
  </svg>
  <div class="abs" style="left:140px;top:33px;font:600 30px/1 'Montserrat',sans-serif;color:#fff">01</div>
  <div class="abs" style="left:114px;top:86px;font:800 17px/1 'Montserrat',sans-serif;color:#fff">Part One.</div>
  <p class="abs tx w j" style="left:114px;top:108px;width:90px;font-size:3.5px">Our Cognac team prepares gift boxes, applies labels and runs quality control for fine spirits and cosmetics, from first sample to final pallet.</p>
  <span class="pg light">03</span>
</section>

<!-- 04 About -->
<section class="slide" style="left:29px;top:227px">
  <div class="abs ph-red" style="left:17px;top:16px;width:154px;height:146px;padding:12px 11px">
    <div style="font:700 11.5px/1.1 'Montserrat',sans-serif;color:#fff">ABOUT OUR<br>COMPANY</div>
    <p class="tx w j" style="margin-top:10px;width:120px">Our Cognac team prepares gift boxes, applies labels and runs quality control for fine spirits and cosmetics, from first sample to final pallet.</p>
    <p class="tx w j" style="margin-top:5px;width:120px">Our Cognac team prepares gift boxes, applies labels and runs quality control for fine spirits and cosmetics, from first sample to final pallet.</p>
  </div>
  <div class="icon-dot" style="left:160px;top:24px"></div>
  <div class="icon-dot" style="left:160px;top:76px"></div>
  <div class="icon-dot" style="left:160px;top:123px"></div>
  <div class="abs" style="left:191px;top:24px;width:112px"><div class="sub">Lorem ipsum</div><p class="tx" style="margin-top:2px">We pack, label and check every bottle with care for premium brands.</p></div>
  <div class="abs" style="left:191px;top:76px;width:112px"><div class="sub">Lorem ipsum</div><p class="tx" style="margin-top:2px">We pack, label and check every bottle with care for premium brands.</p></div>
  <div class="abs" style="left:191px;top:124px;width:112px"><div class="sub">Lorem ipsum</div><p class="tx" style="margin-top:2px">We pack, label and check every bottle with care for premium brands.</p></div>
  <div class="mini-logo"><span class="mini-mark"></span><span>MAISON<br>VALCOUR</span></div>
  <span class="pg">04</span>
</section>

<!-- 05 Education -->
<section class="slide" style="left:359px;top:227px">
  <div class="abs" style="left:13px;top:10px;font:400 11.5px/1 'Montserrat',sans-serif;color:var(--orange)">OUR COMPANY <b style="font-weight:800">EDUCATION</b></div>
  <div class="mini-logo"><span class="mini-mark"></span><span>MAISON<br>VALCOUR</span></div>
  <div class="abs" style="left:48px;top:40px;width:240px;height:90px;background:radial-gradient(ellipse at 50% 50%,#ececec,rgba(255,255,255,0) 70%)" role="img" aria-label="Faint world map in the background"></div>
  <svg class="abs" style="left:0;top:0" width="318" height="178">
    <path d="M120 66 L139 47" stroke="var(--orange)" stroke-width="1.6" fill="none"/>
    <path d="M120 66 L139 106" stroke="var(--orange)" stroke-width="1.6" fill="none"/>
    <circle cx="120" cy="66" r="2.6" fill="var(--orange)"/>
    <path d="M196 66 L216 47" stroke="var(--red)" stroke-width="1.6" fill="none"/>
    <circle cx="196" cy="66" r="2.6" fill="var(--orange)"/>
    <circle cx="139" cy="106" r="2.6" fill="var(--red)"/>
    <circle cx="216" cy="106" r="2.6" fill="var(--red)"/>
  </svg>
  <div class="edu-box or" style="left:63px">
    <svg width="8" height="9" viewBox="0 0 8 9"><circle cx="4" cy="3.5" r="2.8" fill="none" stroke="var(--red)" stroke-width=".8"/><path d="M2.7 7h2.6M3 8.3h2" stroke="var(--red)" stroke-width=".8"/></svg>
    <h4>IDEA</h4><p class="tx c" style="font-size:2.8px">Each order is tracked, checked and delivered on time.</p>
  </div>
  <div class="edu-box" style="left:139px">
    <svg width="9" height="7" viewBox="0 0 9 7"><rect x=".5" y=".5" width="8" height="6" fill="none" stroke="var(--red)" stroke-width=".8"/><path d="M.5 .5l4 3.5 4-3.5" fill="none" stroke="var(--red)" stroke-width=".8"/></svg>
    <h4>PROMOTION</h4><p class="tx c" style="font-size:2.8px">Each order is tracked, checked and delivered on time.</p>
  </div>
  <div class="edu-box" style="left:216px">
    <svg width="9" height="8" viewBox="0 0 9 8"><path d="M.5 .5V7.5H8.5M2 5.5l2-2 1.5 1.5 3-3" fill="none" stroke="var(--red)" stroke-width=".8"/></svg>
    <h4>GROWTH</h4><p class="tx c" style="font-size:2.8px">Each order is tracked, checked and delivered on time.</p>
  </div>
  <p class="abs tx c" style="left:45px;top:143px;width:228px">Our Cognac team prepares gift boxes, applies labels and runs quality control for fine spirits and cosmetics, from first sample to final pallet.</p>
  <span class="pg">05</span>
</section>

<!-- 06 Projects -->
<section class="slide" style="left:688px;top:227px">
  <div class="frame-r" style="left:105px;top:21px;width:63px;height:70px"></div>
  <div class="frame-l" style="left:16px;top:100px;width:44px;height:61px"></div>
  <div class="photo ph-factory" style="left:24px;top:29px;width:135px;height:124px" role="img" aria-label="Photo of a worker labelling bottles on a workbench"></div>
  <div class="abs kick" style="left:182px;top:22px;font-size:7.5px">PORTFOLIO OF</div>
  <div class="abs head" style="left:182px;top:31px">PROJECTS</div>
  <p class="abs tx j" style="left:182px;top:49px;width:105px">Our Cognac team prepares gift boxes, applies labels and runs quality control for fine spirits and cosmetics, from first sample to final pallet.</p>
  <p class="abs tx j" style="left:182px;top:84px;width:105px">Our Cognac team prepares gift boxes, applies labels and runs quality control for fine spirits and cosmetics, from first sample to final pallet.</p>
  <div class="abs bullet" style="left:182px;top:122px;width:105px"><i></i><p class="tx" style="font-size:2.8px">Each order is tracked, checked and delivered on time.</p></div>
  <div class="abs bullet" style="left:182px;top:141px;width:105px"><i style="border-left-color:#e7a4a4"></i><p class="tx" style="font-size:2.8px">Each order is tracked, checked and delivered on time.</p></div>
  <div class="mini-logo"><span class="mini-mark"></span><span>MAISON<br>VALCOUR</span></div>
  <span class="pg">06</span>
</section>

<!-- 07 Overview -->
<section class="slide" style="left:29px;top:418px">
  <div class="abs kick" style="left:14px;top:24px;font-size:10.5px;font-weight:600">COMPANY</div>
  <div class="abs head" style="left:14px;top:35px">OVERVIEW</div>
  <p class="abs tx j" style="left:14px;top:57px;width:124px">Our Cognac team prepares gift boxes, applies labels and runs quality control for fine spirits and cosmetics, from first sample to final pallet.</p>
  <p class="abs tx" style="left:14px;top:81px;width:124px">We pack, label and check every bottle with care for premium brands.</p>
  <svg class="abs" style="left:0;top:0" width="318" height="178" font-family="Open Sans, sans-serif">
    <g stroke="#e1e1e1" stroke-width=".5">
      <line x1="162" y1="22" x2="300" y2="22"/><line x1="162" y1="34" x2="300" y2="34"/><line x1="162" y1="47" x2="300" y2="47"/><line x1="162" y1="59" x2="300" y2="59"/><line x1="162" y1="71" x2="300" y2="71"/><line x1="162" y1="84" x2="300" y2="84"/><line x1="300" y1="22" x2="300" y2="96"/>
    </g>
    <line x1="162" y1="96" x2="300" y2="96" stroke="#999" stroke-width=".6"/>
    <g font-size="4" fill="#555" text-anchor="end">
      <text x="159" y="23.5">60</text><text x="159" y="35.5">50</text><text x="159" y="48.5">40</text><text x="159" y="60.5">30</text><text x="159" y="72.5">20</text><text x="159" y="85.5">10</text><text x="159" y="97.5">0</text>
    </g>
    <g>
      <rect x="177" y="47" width="3.6" height="49" fill="var(--orange)"/><rect x="182.5" y="34.5" width="3.6" height="61.5" fill="var(--red)"/>
      <rect x="207" y="82.5" width="3.6" height="13.5" fill="var(--orange)"/><rect x="212.5" y="53" width="3.6" height="43" fill="var(--red)"/>
      <rect x="236" y="24" width="3.6" height="72" fill="var(--orange)"/><rect x="241.5" y="80" width="3.6" height="16" fill="var(--red)"/>
      <rect x="266" y="32" width="3.6" height="64" fill="var(--red)"/><rect x="271.5" y="59" width="3.6" height="37" fill="var(--orange)"/>
    </g>
    <g font-size="4.3" fill="#444" text-anchor="middle">
      <text x="183" y="104">JAN</text><text x="213" y="104">FEB</text><text x="242" y="104">MAR</text><text x="271" y="104">APR</text>
    </g>
    <g stroke="#e4e4e4" stroke-width=".4">
      <line x1="20" y1="108" x2="142" y2="108"/><line x1="20" y1="115.5" x2="142" y2="115.5"/><line x1="20" y1="123" x2="142" y2="123"/><line x1="20" y1="130.5" x2="142" y2="130.5"/><line x1="20" y1="138" x2="142" y2="138"/><line x1="20" y1="145.5" x2="142" y2="145.5"/>
      <line x1="142" y1="108" x2="142" y2="153"/>
    </g>
    <line x1="20" y1="153" x2="142" y2="153" stroke="#999" stroke-width=".5"/>
    <g font-size="3" fill="#555" text-anchor="end">
      <text x="18" y="109">60</text><text x="18" y="116.5">50</text><text x="18" y="124">40</text><text x="18" y="131.5">30</text><text x="18" y="139">20</text><text x="18" y="146.5">10</text><text x="18" y="154">0</text>
    </g>
    <polyline points="29,146 42,151 55,140 68,132 81,146 94,132 108,140 121,138 134,131" fill="none" stroke="var(--red)" stroke-width=".7"/>
    <polyline points="29,151 42,149 55,137 68,128 81,141 94,138 108,136 121,132 134,146" fill="none" stroke="var(--orange)" stroke-width=".7"/>
    <g font-size="2.3" fill="#666" text-anchor="middle">
      <text x="29" y="158">TEXT 01</text><text x="42" y="158">TEXT 02</text><text x="55" y="158">TEXT 03</text><text x="68" y="158">TEXT 04</text><text x="81" y="158">TEXT 05</text><text x="94" y="158">TEXT 06</text><text x="108" y="158">TEXT 07</text><text x="121" y="158">TEXT 08</text><text x="134" y="158">TEXT 09</text>
    </g>
  </svg>
  <div class="abs legend" style="left:153px;top:111px;width:66px"><h5>Lorem ipsum</h5><p class="tx" style="font-size:2.6px">Short note on monthly volume.</p></div>
  <div class="abs legend" style="left:236px;top:111px;width:66px"><h5 class="r">Lorem ipsum</h5><p class="tx" style="font-size:2.6px">Short note on monthly volume.</p></div>
  <div class="abs legend" style="left:153px;top:136px;width:66px"><h5 class="r">Lorem ipsum</h5><p class="tx" style="font-size:2.6px">Short note on monthly volume.</p></div>
  <div class="abs legend" style="left:236px;top:136px;width:66px"><h5>Lorem ipsum</h5><p class="tx" style="font-size:2.6px">Short note on monthly volume.</p></div>
  <div class="mini-logo"><span class="mini-mark"></span><span>MAISON<br>VALCOUR</span></div>
  <span class="pg">07</span>
</section>

<!-- 08 Product -->
<section class="slide" style="left:359px;top:418px">
  <div class="photo ph-line" style="left:0;top:0;width:318px;height:178px" role="img" aria-label="Photo of two workers in masks on a bottle filling line"></div>
  <div class="abs ph-red" style="left:26px;top:0;width:126px;height:178px;padding:20px 7px 0 7px">
    <div style="font:400 7.5px/1 'Montserrat',sans-serif;color:#fff">PORTFOLIO OF</div>
    <div style="font:900 15.5px/1 'Montserrat',sans-serif;color:var(--orange);margin-top:3px">PRODUCT</div>
    <p class="tx w j" style="margin-top:4px">Our Cognac team prepares gift boxes, applies labels and runs quality control for fine spirits and cosmetics, from first sample to final pallet.</p>
    <p class="tx w j" style="margin-top:5px">Our Cognac team prepares gift boxes, applies labels and runs quality control for fine spirits and cosmetics, from first sample to final pallet.</p>
    <div class="bullet" style="margin-top:8px"><i style="border-left-color:var(--orange)"></i><p class="tx w" style="font-size:2.8px">Each order is tracked, checked and delivered on time.</p></div>
    <div class="bullet" style="margin-top:9px"><i style="border-left-color:var(--orange)"></i><p class="tx w" style="font-size:2.8px">Each order is tracked, checked and delivered on time.</p></div>
  </div>
  <div class="mini-logo on-red"><span class="mini-mark"></span><span>MAISON<br>VALCOUR</span></div>
  <span class="pg" style="background:#fff">08</span>
</section>

<!-- 09 Summary -->
<section class="slide" style="left:688px;top:418px">
  <div class="abs" style="left:13px;top:20px;font:600 9.5px/1 'Montserrat',sans-serif;color:var(--orange)">COMPANY <b style="font:800 13px/1 'Montserrat',sans-serif;color:var(--red)">SUMMARY</b></div>
  <p class="abs tx" style="left:13px;top:43px;width:110px;font-size:4px;color:#333">We pack, label and check every bottle with care for premium brands.</p>
  <div class="abs legend" style="left:13px;top:76px;width:75px"><h5 class="r" style="font-size:5.2px">Lorem ipsum</h5><p class="tx" style="font-size:2.7px">Each order is tracked, checked and delivered on time.</p></div>
  <div class="abs legend" style="left:13px;top:104px;width:75px"><h5 style="font-size:5.2px">Lorem ipsum</h5><p class="tx" style="font-size:2.7px">Each order is tracked, checked and delivered on time.</p></div>
  <div class="abs legend" style="left:13px;top:132px;width:75px"><h5 class="r" style="font-size:5.2px">Lorem ipsum</h5><p class="tx" style="font-size:2.7px">Each order is tracked, checked and delivered on time.</p></div>
  <svg class="abs" style="left:0;top:0" width="318" height="178" font-family="Montserrat, sans-serif">
    <path d="M142 72 A58 58 0 1 1 165 130" fill="none" stroke="#333" stroke-width="3"/>
    <path d="M138 66 L142 80 L148 68" fill="none" stroke="#333" stroke-width="2"/>
    <circle cx="145" cy="110" r="3" fill="#333"/>
    <circle cx="242" cy="55" r="16" fill="var(--red)"/><circle cx="242" cy="55" r="10.5" fill="#fff"/><circle cx="242" cy="55" r="8.5" fill="var(--red)"/>
    <circle cx="241" cy="54" r="2.5" fill="none" stroke="#fff" stroke-width=".9"/><path d="M242.8 55.8l2 2" stroke="#fff" stroke-width=".9"/>
    <circle cx="253" cy="108" r="14" fill="var(--orange)"/><circle cx="253" cy="108" r="9.5" fill="#fff"/><circle cx="253" cy="108" r="7.5" fill="var(--orange)"/>
    <circle cx="253" cy="107" r="2.4" fill="#fff"/>
    <circle cx="226" cy="143" r="11" fill="var(--red)"/><circle cx="226" cy="143" r="7.5" fill="#fff"/><circle cx="226" cy="143" r="6" fill="var(--red)"/>
    <circle cx="158" cy="128" r="8" fill="var(--orange)"/><circle cx="158" cy="128" r="5.4" fill="#fff"/><circle cx="158" cy="128" r="4.2" fill="var(--orange)"/>
    <g stroke="var(--red)" stroke-width=".5" fill="none"><path d="M256 48 L270 43"/><path d="M239 108 L228 104"/><path d="M234 152 L245 157"/></g>
    <path d="M166 128 L178 126" stroke="var(--orange)" stroke-width=".5"/>
    <g font-size="3.3" font-style="italic" font-weight="700"><text x="271" y="44" fill="var(--red)">85%</text><text x="214" y="105" fill="var(--orange)">80%</text><text x="246" y="160" fill="var(--red)">75%</text><text x="179" y="128" fill="var(--orange)">50%</text></g>
    <rect x="180" y="72" width="1.8" height="7" fill="#333"/><rect x="183" y="70" width="1.8" height="9" fill="#333"/><rect x="186" y="74" width="1.8" height="5" fill="#333"/>
    <text x="184" y="87" font-size="4.6" font-weight="700" fill="#333" text-anchor="middle">MAIN TITLE</text>
    <text x="184" y="91" font-size="2.4" fill="#555" text-anchor="middle">Short note here.</text>
    <g font-size="4.4" font-weight="600" fill="var(--red)">
      <text x="278" y="51">Your Title</text><text x="284" y="99">Your Title</text><text x="272" y="141">Your Title</text><text x="128" y="139">Your Title</text>
    </g>
    <g font-size="2.3" fill="#555"><text x="278" y="55">Short note here.</text><text x="284" y="103">Short note here.</text><text x="272" y="145">Short note here.</text><text x="128" y="143">Short note here.</text></g>
  </svg>
  <div class="mini-logo"><span class="mini-mark"></span><span>MAISON<br>VALCOUR</span></div>
  <span class="pg">09</span>
</section>

<!-- 10 Benefits -->
<section class="slide" style="left:29px;top:611px">
  <div class="frame-l" style="left:8px;top:102px;width:62px;height:67px"></div>
  <div class="photo ph-cognac" style="left:15px;top:21px;width:128px;height:141px" role="img" aria-label="Photo of hands holding a cognac decanter"></div>
  <div class="abs kick" style="left:153px;top:22px;font-weight:300;font-size:11px">BENEFITS TO EACH</div>
  <div class="abs" style="left:153px;top:36px;font:800 11px/1 'Montserrat',sans-serif;color:var(--red)">CUSTOMER SEGMENTS</div>
  <div class="abs" style="left:153px;top:54px;width:150px">
    <p class="tx j">Our Cognac team prepares gift boxes, applies labels and runs quality control for fine spirits and cosmetics, from first sample to final pallet.</p>
    <p class="tx j" style="margin-top:4px">Our Cognac team prepares gift boxes, applies labels and runs quality control for fine spirits and cosmetics, from first sample to final pallet.</p>
    <p class="tx j" style="margin-top:4px">Our Cognac team prepares gift boxes, applies labels and runs quality control for fine spirits and cosmetics, from first sample to final pallet.</p>
    <p class="tx j" style="margin-top:4px">Our Cognac team prepares gift boxes, applies labels and runs quality control for fine spirits and cosmetics, from first sample to final pallet.</p>
    <p class="tx j" style="margin-top:4px">Our Cognac team prepares gift boxes, applies labels and runs quality control for fine spirits and cosmetics, from first sample to final pallet.</p>
  </div>
  <div class="mini-logo"><span class="mini-mark"></span><span>MAISON<br>VALCOUR</span></div>
  <span class="pg">10</span>
</section>

<!-- 11 Price -->
<section class="slide" style="left:359px;top:611px">
  <div class="abs" style="left:0;top:20px;width:318px;text-align:center;font:400 13px/1 'Montserrat',sans-serif;color:var(--orange)">PRICE <b style="font-weight:800;color:var(--red)">PRESENTATION</b></div>
  <p class="abs tx c" style="left:28px;top:38px;width:262px">Our Cognac team prepares gift boxes, applies labels and runs quality control for fine spirits and cosmetics, from first sample to final pallet.</p>
  <p class="abs tx c" style="left:28px;top:52px;width:262px">Our Cognac team prepares gift boxes, applies labels and runs quality control for fine spirits and cosmetics, from first sample to final pallet.</p>
  <svg class="abs" style="left:0;top:0" width="318" height="178" font-family="Montserrat, sans-serif">
    <line x1="31" y1="105" x2="160" y2="105" stroke="var(--orange)" stroke-width="3"/>
    <line x1="160" y1="105" x2="282" y2="105" stroke="var(--red)" stroke-width="3"/>
    <path d="M280 101 L288 105 L280 109 Z" fill="var(--red)"/>
    <g fill="none" stroke-width="4.5">
      <path d="M66 102 A16 16 0 1 1 94 102" stroke="var(--orange)"/>
      <path d="M119 102 A16 16 0 1 1 147 102" stroke="var(--red)"/>
      <path d="M172 102 A16 16 0 1 1 200 102" stroke="var(--orange)"/>
      <path d="M225 102 A16 16 0 1 1 253 102" stroke="var(--red)"/>
    </g>
    <g fill="#fff" stroke-width="1.6">
      <circle cx="80" cy="92" r="10" stroke="var(--orange)"/><circle cx="133" cy="92" r="10" stroke="var(--red)"/>
      <circle cx="186" cy="92" r="10" stroke="var(--orange)"/><circle cx="239" cy="92" r="10" stroke="var(--red)"/>
    </g>
    <circle cx="80" cy="92" r="5" fill="none" stroke="var(--red)" stroke-width=".8"/><path d="M80 89v3l2 1.5" stroke="var(--red)" stroke-width=".8" fill="none"/>
    <circle cx="133" cy="93" r="4.5" fill="var(--orange)"/><text x="133" y="95" font-size="4.5" font-weight="700" fill="#fff" text-anchor="middle">$</text>
    <g fill="none" stroke="var(--red)" stroke-width=".8"><ellipse cx="186" cy="89" rx="4.5" ry="1.5"/><path d="M181.5 89v6c0 2 9 2 9 0v-6M181.5 92c0 2 9 2 9 0"/></g>
    <circle cx="238" cy="90.5" r="3.5" fill="none" stroke="var(--red)" stroke-width=".9"/><path d="M236 93l-2.5 3" stroke="var(--red)" stroke-width=".9"/>
    <g font-size="3.6" font-weight="700" fill="#fff" text-anchor="middle">
      <text x="108" y="106.3">Step 01</text><text x="161" y="106.3">Step 02</text><text x="214" y="106.3">Step 03</text><text x="267" y="106.3">Step 04</text>
    </g>
    <g stroke="#888" stroke-width=".5"><line x1="80" y1="111" x2="80" y2="120"/><line x1="133" y1="111" x2="133" y2="120"/><line x1="186" y1="111" x2="186" y2="120"/><line x1="239" y1="111" x2="239" y2="120"/></g>
    <g fill="#888"><circle cx="80" cy="120" r=".9"/><circle cx="133" cy="120" r=".9"/><circle cx="186" cy="120" r=".9"/><circle cx="239" cy="120" r=".9"/></g>
  </svg>
  <div class="abs" style="left:56px;top:124px;width:48px;text-align:center"><div class="sub" style="color:var(--red)">Lorem Ipsum</div><p class="tx c" style="font-size:2.6px;margin-top:2px">Short note on this step.</p></div>
  <div class="abs" style="left:109px;top:124px;width:48px;text-align:center"><div class="sub">Lorem Ipsum</div><p class="tx c" style="font-size:2.6px;margin-top:2px">Short note on this step.</p></div>
  <div class="abs" style="left:162px;top:124px;width:48px;text-align:center"><div class="sub" style="color:var(--red)">Lorem Ipsum</div><p class="tx c" style="font-size:2.6px;margin-top:2px">Short note on this step.</p></div>
  <div class="abs" style="left:215px;top:124px;width:48px;text-align:center"><div class="sub">Lorem Ipsum</div><p class="tx c" style="font-size:2.6px;margin-top:2px">Short note on this step.</p></div>
  <div class="mini-logo"><span class="mini-mark"></span><span>MAISON<br>VALCOUR</span></div>
  <span class="pg">11</span>
</section>

<!-- 12 Active Intelligence -->
<section class="slide" style="left:688px;top:611px">
  <div class="abs" style="left:22px;top:14px;width:66px;height:2px;background:var(--red)"></div>
  <div class="photo ph-factory" style="left:0;top:20px;width:182px;height:135px" role="img" aria-label="Photo of a warehouse floor with cognac bottles on a conveyor"></div>
  <div class="abs" style="left:6px;top:150px;width:40px;height:2px;background:var(--red)"></div>
  <div class="abs kick" style="left:197px;top:23px;font-size:10px;font-weight:600">ACTIVE</div>
  <div class="abs" style="left:197px;top:35px;font:800 10px/1 'Montserrat',sans-serif;color:var(--red)">INTELLIGENCE</div>
  <p class="abs tx j" style="left:197px;top:50px;width:103px">Our Cognac team prepares gift boxes, applies labels and runs quality control for fine spirits and cosmetics, from first sample to final pallet.</p>
  <p class="abs tx j" style="left:197px;top:84px;width:103px">Our Cognac team prepares gift boxes, applies labels and runs quality control for fine spirits and cosmetics, from first sample to final pallet.</p>
  <div class="abs bullet" style="left:197px;top:122px;width:103px"><i style="border-left-color:var(--orange)"></i><p class="tx" style="font-size:2.8px">Each order is tracked, checked and delivered on time.</p></div>
  <div class="abs bullet" style="left:197px;top:141px;width:103px"><i style="border-left-color:#f6c98a"></i><p class="tx" style="font-size:2.8px">Each order is tracked, checked and delivered on time.</p></div>
  <div class="mini-logo"><span class="mini-mark"></span><span>MAISON<br>VALCOUR</span></div>
  <span class="pg">12</span>
</section>

<!-- 13 Roadmap -->
<section class="slide" style="left:29px;top:800px">
  <div class="abs" style="left:8px;top:7px;width:64px;height:64px;border-top:2px solid var(--red);border-left:2px solid var(--red)"></div>
  <svg class="abs" style="left:0;top:0" width="318" height="178" font-family="Montserrat, sans-serif">
    <path d="M293 137 C250 137 205 132 189 120 C180 112 182 100 182 90" fill="none" stroke="var(--red)" stroke-width="1.5"/>
    <circle cx="293" cy="137" r="2" fill="#333"/>
    <line x1="293" y1="135" x2="293" y2="108" stroke="#333" stroke-width="1" stroke-dasharray="1 1.5"/>
    <line x1="182" y1="90" x2="182" y2="78" stroke="#333" stroke-width="1" stroke-dasharray="1 1.5"/>
    <circle cx="182" cy="90" r="1.8" fill="#333"/>
    <path d="M185 58 C195 52 215 62 229 52" fill="none" stroke="#333" stroke-width=".9" stroke-dasharray="1 1.5"/>
    <path d="M178 55 C168 48 152 55 143 49" fill="none" stroke="var(--red)" stroke-width="1.3"/>
    <path d="M140 36 C145 30 155 32 163 30" fill="none" stroke="#333" stroke-width=".9" stroke-dasharray="1 1.5"/>
    <path d="M293 106 L286 99 A21 21 0 1 1 300 99 Z" fill="#333"/><circle cx="293" cy="82" r="17" fill="#fff"/>
    <text x="293" y="92" font-size="25" font-weight="600" fill="var(--orange)" text-anchor="middle">1</text>
    <path d="M182 77 L178 72 A13 13 0 1 1 186 72 Z" fill="#333"/><circle cx="182" cy="62" r="10.5" fill="#fff"/>
    <text x="182" y="68" font-size="15" font-weight="600" fill="var(--red)" text-anchor="middle">2</text>
    <path d="M231 53 L228 49 A10 10 0 1 1 234 49 Z" fill="#333"/><circle cx="231" cy="41" r="8" fill="#fff"/>
    <text x="231" y="45.5" font-size="11" font-weight="600" fill="var(--orange)" text-anchor="middle">3</text>
    <path d="M140 48 L138 45 A7 7 0 1 1 142 45 Z" fill="#333"/><circle cx="140" cy="40" r="5.5" fill="#fff"/>
    <text x="140" y="43" font-size="8" font-weight="600" fill="var(--orange)" text-anchor="middle">4</text>
    <circle cx="164" cy="28" r="4.5" fill="#333"/><circle cx="164" cy="28" r="3.3" fill="#fff"/>
    <text x="164" y="30" font-size="5" font-weight="600" fill="var(--orange)" text-anchor="middle">5</text>
    <circle cx="118" cy="28" r="3.8" fill="#333"/><circle cx="118" cy="28" r="2.8" fill="#fff"/>
    <text x="118" y="29.8" font-size="4" font-weight="600" fill="var(--orange)" text-anchor="middle">4</text>
  </svg>
  <div class="abs" style="left:74px;top:26px;width:40px"><div class="sub" style="font-size:4.2px">LOREM IPSUM</div><p class="tx" style="font-size:2.3px;margin-top:1px">Short note on this stage.</p></div>
  <div class="abs" style="left:175px;top:20px;width:40px"><div class="sub" style="font-size:4.2px">LOREM IPSUM</div><p class="tx" style="font-size:2.3px;margin-top:1px">Short note on this stage.</p></div>
  <div class="abs" style="left:246px;top:22px;width:40px"><div class="sub" style="font-size:4.2px">LOREM IPSUM</div><p class="tx" style="font-size:2.3px;margin-top:1px">Short note on this stage.</p></div>
  <div class="abs" style="left:129px;top:77px;width:40px"><div class="sub" style="font-size:4.2px">LOREM IPSUM</div><p class="tx" style="font-size:2.3px;margin-top:1px">Short note on this stage.</p></div>
  <div class="abs" style="left:234px;top:93px;width:40px"><div class="sub" style="font-size:4.2px">LOREM IPSUM</div><p class="tx" style="font-size:2.3px;margin-top:1px">Short note on this stage.</p></div>
  <div class="abs kick" style="left:35px;top:87px;font-weight:300;font-size:9.5px;letter-spacing:.8px">TIMELINE OF</div>
  <div class="abs" style="left:35px;top:98px;font:800 15px/1 'Montserrat',sans-serif;color:var(--red)">ROADMAP</div>
  <div class="abs" style="left:36px;top:116px;font:600 7.5px/1 'Montserrat',sans-serif;color:var(--orange)">FOR 2 YEARS</div>
  <div class="abs" style="left:35px;top:138px;display:flex;gap:4px;align-items:center">
    <span style="width:15px;height:15px;border-radius:50%;background:var(--red);color:#fff;font:800 9px/15px 'Montserrat',sans-serif;text-align:center">A</span>
    <div><div style="font:700 8px/1 'Montserrat',sans-serif;color:var(--orange)">2019</div><p class="tx" style="font-size:2.2px">Short note.</p></div>
  </div>
  <div class="abs" style="left:105px;top:138px;display:flex;gap:4px;align-items:center">
    <span style="width:15px;height:15px;border-radius:50%;background:var(--red);color:#fff;font:800 9px/15px 'Montserrat',sans-serif;text-align:center">B</span>
    <div><div style="font:700 8px/1 'Montserrat',sans-serif;color:var(--orange)">2020</div><p class="tx" style="font-size:2.2px">Short note.</p></div>
  </div>
  <div class="mini-logo"><span class="mini-mark"></span><span>MAISON<br>VALCOUR</span></div>
  <span class="pg">13</span>
</section>

<!-- 14 Two columns -->
<section class="slide" style="left:359px;top:800px">
  <div class="abs ph-red" style="left:15px;top:15px;width:147px;height:148px;padding:9px 10px 0">
    <div style="font:600 9.5px/1.05 'Montserrat',sans-serif;color:#fff">LOREM IPSUM<br><b style="font-weight:800">DOLOR SIT AMET</b></div>
    <p class="tx w j" style="margin-top:6px">Our Cognac team prepares gift boxes, applies labels and runs quality control for fine spirits and cosmetics, from first sample to final pallet.</p>
    <p class="tx w j" style="margin-top:5px">Our Cognac team prepares gift boxes, applies labels and runs quality control for fine spirits and cosmetics, from first sample to final pallet.</p>
    <div class="bullet w" style="margin-top:8px"><i></i><p class="tx w" style="font-size:2.8px">Each order is tracked, checked and delivered on time.</p></div>
    <div class="bullet w" style="margin-top:8px"><i></i><p class="tx w" style="font-size:2.8px">Each order is tracked, checked and delivered on time.</p></div>
  </div>
  <div class="abs" style="left:171px;top:24px;width:132px">
    <div style="font:600 9.5px/1.05 'Montserrat',sans-serif;color:var(--orange)">LOREM IPSUM<br><b style="font-weight:800;color:var(--red)">DOLOR SIT AMET</b></div>
    <p class="tx j" style="margin-top:6px">Our Cognac team prepares gift boxes, applies labels and runs quality control for fine spirits and cosmetics, from first sample to final pallet.</p>
    <p class="tx j" style="margin-top:5px">Our Cognac team prepares gift boxes, applies labels and runs quality control for fine spirits and cosmetics, from first sample to final pallet.</p>
    <div class="bullet" style="margin-top:8px"><i></i><p class="tx" style="font-size:2.8px">Each order is tracked, checked and delivered on time.</p></div>
    <div class="bullet" style="margin-top:8px"><i style="border-left-color:#e7a4a4"></i><p class="tx" style="font-size:2.8px">Each order is tracked, checked and delivered on time.</p></div>
  </div>
  <div class="mini-logo"><span class="mini-mark"></span><span>MAISON<br>VALCOUR</span></div>
  <span class="pg">14</span>
</section>

<!-- 15 Timeline infographic -->
<section class="slide" style="left:688px;top:800px">
  <div class="abs" style="left:0;top:18px;width:318px;text-align:center;font:400 11px/1 'Montserrat',sans-serif;letter-spacing:2.6px;color:var(--orange)">TIMELINE <b style="font-weight:700">INFOGRAPHIC</b></div>
  <svg class="abs" style="left:0;top:0" width="318" height="178" font-family="Montserrat, sans-serif">
    <line x1="45" y1="101" x2="277" y2="101" stroke="#555" stroke-width=".8"/>
    <g fill="none" stroke-width="1.4">
      <path d="M55 101 V76 Q55 70 61 70 H89 Q95 70 95 76 V101" stroke="var(--red)"/>
      <path d="M140 101 V76 Q140 70 146 70 H174 Q180 70 180 76 V101" stroke="var(--red)"/>
      <path d="M223 101 V76 Q223 70 229 70 H257 Q263 70 263 76 V101" stroke="var(--red)"/>
      <path d="M97 101 V126 Q97 132 103 132 H131 Q137 132 137 126 V101" stroke="var(--orange)"/>
      <path d="M180 101 V126 Q180 132 186 132 H214 Q220 132 220 126 V101" stroke="var(--orange)"/>
    </g>
    <g><circle cx="75" cy="68" r="7" fill="#fff" stroke="var(--red)" stroke-width="1.2"/><circle cx="75" cy="68" r="4.5" fill="var(--red)"/>
      <circle cx="160" cy="68" r="7" fill="#fff" stroke="var(--red)" stroke-width="1.2"/><circle cx="160" cy="68" r="4.5" fill="var(--red)"/>
      <circle cx="243" cy="68" r="7" fill="#fff" stroke="var(--red)" stroke-width="1.2"/><circle cx="243" cy="68" r="4.5" fill="var(--red)"/>
      <circle cx="117" cy="134" r="7" fill="#fff" stroke="var(--orange)" stroke-width="1.2"/><circle cx="117" cy="134" r="4.5" fill="var(--orange)"/>
      <circle cx="200" cy="134" r="7" fill="#fff" stroke="var(--orange)" stroke-width="1.2"/><circle cx="200" cy="134" r="4.5" fill="var(--orange)"/></g>
    <g font-size="10" fill="#333" text-anchor="middle"><text x="75" y="92">2018</text><text x="160" y="92">2020</text><text x="243" y="92">2022</text><text x="117" y="118">2019</text><text x="200" y="118">2021</text></g>
    <g fill="var(--red)"><rect x="114" y="60" width="1.5" height="3"/><rect x="116.5" y="58" width="1.5" height="5"/><rect x="119" y="56" width="1.5" height="7"/>
      <circle cx="200" cy="58" r="3" fill="none" stroke="var(--red)" stroke-width="1"/>
      <circle cx="75" cy="103" r="0"/></g>
    <circle cx="160" cy="109" r="2.2" fill="none" stroke="var(--orange)" stroke-width=".9"/>
    <text x="243" y="111" font-size="6" font-weight="700" fill="var(--orange)" text-anchor="middle">$</text>
    <g font-size="3.2" font-weight="700" fill="#333" text-anchor="middle"><text x="117" y="67">LOREM IPSUM</text><text x="200" y="67">LOREM IPSUM</text><text x="75" y="109">LOREM IPSUM</text><text x="160" y="118">LOREM IPSUM</text><text x="243" y="118">LOREM IPSUM</text></g>
  </svg>
  <p class="abs tx c" style="left:103px;top:70px;width:28px;font-size:2.6px">Short note on this year.</p>
  <p class="abs tx c" style="left:186px;top:70px;width:28px;font-size:2.6px">Short note on this year.</p>
  <p class="abs tx c" style="left:61px;top:112px;width:28px;font-size:2.6px">Short note on this year.</p>
  <p class="abs tx c" style="left:146px;top:121px;width:28px;font-size:2.6px">Short note on this year.</p>
  <p class="abs tx c" style="left:229px;top:121px;width:28px;font-size:2.6px">Short note on this year.</p>
  <div class="mini-logo"><span class="mini-mark"></span><span>MAISON<br>VALCOUR</span></div>
  <span class="pg">15</span>
</section>

<!-- 16 Domain -->
<section class="slide" style="left:29px;top:991px">
  <div class="abs ph-red" style="left:17px;top:0;width:141px;height:178px;padding:22px 9px 0">
    <div style="font:600 10px/1.05 'Montserrat',sans-serif;color:#fff">LOREM IPSUM<br><b style="font-weight:800">DOLOR SIT AMET</b></div>
    <p class="tx w j" style="margin-top:5px">Our Cognac team prepares gift boxes, applies labels and runs quality control for fine spirits and cosmetics, from first sample to final pallet.</p>
    <p class="tx w j" style="margin-top:5px">Our Cognac team prepares gift boxes, applies labels and runs quality control for fine spirits and cosmetics, from first sample to final pallet.</p>
    <div class="bullet w" style="margin-top:8px"><i></i><p class="tx w" style="font-size:2.8px">Each order is tracked, checked and delivered on time.</p></div>
    <div class="bullet w" style="margin-top:8px"><i style="border-left-color:rgba(255,255,255,.6)"></i><p class="tx w" style="font-size:2.8px">Each order is tracked, checked and delivered on time.</p></div>
  </div>
  <div class="abs" style="left:171px;top:28px;font:600 9.3px/1.4 'Montserrat',sans-serif;color:var(--orange)">WHAT'S A DOMAIN?<br>IT'S THAT NAME UP<br><b style="font-weight:800;color:var(--red)">IN THE ADDRESS BAR.</b></div>
  <div class="check" style="top:73px"><svg width="6" height="6" viewBox="0 0 6 6"><path d="M.6 3.2l1.7 1.7L5.4 1" fill="none" stroke="#333" stroke-width=".9"/></svg>Fits your business or products</div>
  <div class="check" style="top:86.7px"><svg width="6" height="6" viewBox="0 0 6 6"><path d="M.6 3.2l1.7 1.7L5.4 1" fill="none" stroke="#333" stroke-width=".9"/></svg>Is easy to spell and remember</div>
  <div class="check" style="top:100.4px"><svg width="6" height="6" viewBox="0 0 6 6"><path d="M.6 3.2l1.7 1.7L5.4 1" fill="none" stroke="#333" stroke-width=".9"/></svg>Fits your business or products</div>
  <div class="check" style="top:114.1px"><svg width="6" height="6" viewBox="0 0 6 6"><path d="M.6 3.2l1.7 1.7L5.4 1" fill="none" stroke="#333" stroke-width=".9"/></svg>Is easy to spell and remember</div>
  <div class="check" style="top:127.8px"><svg width="6" height="6" viewBox="0 0 6 6"><path d="M.6 3.2l1.7 1.7L5.4 1" fill="none" stroke="#333" stroke-width=".9"/></svg>Fits your business or products</div>
  <div class="check" style="top:141.5px"><svg width="6" height="6" viewBox="0 0 6 6"><path d="M.6 3.2l1.7 1.7L5.4 1" fill="none" stroke="#333" stroke-width=".9"/></svg>Is easy to spell and remember</div>
  <div class="mini-logo"><span class="mini-mark"></span><span>MAISON<br>VALCOUR</span></div>
  <span class="pg">16</span>
</section>

<!-- 17 Team -->
<section class="slide" style="left:359px;top:991px">
  <div class="abs" style="left:0;top:26px;width:318px;text-align:center;font:600 10px/1 'Montserrat',sans-serif;color:var(--coral)">TEAM MEMBERS <b style="font-weight:800">AND ADVISORS</b></div>
  <p class="abs tx c" style="left:18px;top:40px;width:282px">Our Cognac team prepares gift boxes, applies labels and runs quality control for fine spirits and cosmetics, from first sample to final pallet.</p>
  <p class="abs tx c" style="left:18px;top:57px;width:282px">We pack, label and check every bottle with care for premium brands.</p>
  <div class="abs ph-red" style="left:0;top:74px;width:318px;height:74px"></div>
  <div class="member" style="left:19px"><div class="avatar" role="img" aria-label="Team member portrait"></div><h6>THEO MARLIN</h6><p class="tx w c" style="font-size:2.4px">Each order is tracked, checked and delivered on time.</p></div>
  <div class="member" style="left:95px"><div class="avatar" role="img" aria-label="Team member portrait"></div><h6>INES ROCHARD</h6><p class="tx w c" style="font-size:2.4px">Each order is tracked, checked and delivered on time.</p></div>
  <div class="member" style="left:169px"><div class="avatar" role="img" aria-label="Team member portrait"></div><h6>THEO MARLIN</h6><p class="tx w c" style="font-size:2.4px">Each order is tracked, checked and delivered on time.</p></div>
  <div class="member" style="left:245px"><div class="avatar" role="img" aria-label="Team member portrait"></div><h6>INES ROCHARD</h6><p class="tx w c" style="font-size:2.4px">Each order is tracked, checked and delivered on time.</p></div>
  <div class="mini-logo"><span class="mini-mark"></span><span>MAISON<br>VALCOUR</span></div>
  <span class="pg">17</span>
</section>

<!-- 18 Thank you -->
<section class="slide ph-red" style="left:688px;top:991px" role="img" aria-label="Red tinted photo of a bottle packing line">
  <div class="abs" style="left:199px;top:64px;width:119px;height:114px;background:#fff"></div>
  <div class="abs brand" style="left:205px;top:80px">
    <span class="brand-square" style="width:20px;height:20px"></span>
    <span class="brand-name" style="font-size:10px">MAISON<br>VALCOUR</span>
  </div>
  <div class="abs" style="left:17px;top:48px;font:900 17.5px/1 'Montserrat',sans-serif;color:#fff">THANK YOU</div>
  <div class="abs" style="left:17px;top:79px;font:800 10px/1 'Montserrat',sans-serif;color:#fff">CONTACT US</div>
  <div class="abs" style="left:17px;top:94px;font:400 6.5px/1.55 'Open Sans',sans-serif;color:#fff">
    <div style="display:flex;gap:3px;align-items:center"><svg width="5" height="5" viewBox="0 0 5 5"><circle cx="2.5" cy="2.5" r="2.5" fill="#fff"/><path d="M1.5 1.3c0 1.3.9 2.2 2.2 2.2" stroke="var(--red)" stroke-width=".7" fill="none"/></svg>555-014-2290</div>
    <div style="display:flex;gap:3px;align-items:center"><svg width="5" height="5" viewBox="0 0 5 5"><circle cx="2.5" cy="2.5" r="2.5" fill="#fff"/><rect x="1.2" y="1.6" width="2.6" height="1.8" fill="none" stroke="var(--red)" stroke-width=".5"/></svg>info@maisonvalcour.com</div>
    <div style="display:flex;gap:3px;align-items:center"><svg width="5" height="5" viewBox="0 0 5 5"><circle cx="2.5" cy="2.5" r="2.5" fill="#fff"/><circle cx="2.5" cy="2.2" r=".8" fill="var(--red)"/></svg>Your address, your city, box 88900</div>
  </div>
  <div class="abs url" style="left:17px;top:136px;color:#fff">www.maisonvalcour.com</div>
  <div class="abs social" style="left:242px;top:154px;gap:6px"><span style="width:11px;height:11px"></span><span style="width:11px;height:11px"></span><span style="width:11px;height:11px"></span><span style="width:11px;height:11px"></span></div>
</section>

</body>
</html>
```